We need a refreshed business card. Our company is a venture capital investment firm focused on investing in medical devices. Logo is attached. please also see our website www.velmoracapital.example

Target Market(s)

investors and potential investment targets

Industry/Entity Type

medical investments

Contact Information for Business Card

logo, name, title, email, phone, website, address,

Colors
0054AA
0677BA
7BADD7
CADEEF
E8F1F8
0094D4
00A9DD
6FCCEA
C7EBF8
E9F6FB
00AB8E
00BBA5
67D7C9
C6EFE9
E9F9F6

Requirements
Must have
• fresh modern design
Nice to have
• QR code leading to our linked in page, short description of what we do “Early Stage Medical Device Investors”

```html
<!DOCTYPE html>
<html lang="en">
<head>
<meta charset="utf-8">
<title>Velmora Business Card</title>
<link href="https://fonts.googleapis.com/css2?family=Lato:wght@400;700&display=swap" rel="stylesheet">
<style>
  :root {
    --backdrop: #1e1e1f;
    --brand-blue: #0054aa;
    --brand-blue-deep: #003d8c;
    --brand-blue-mid: #0a56a6;
    --brand-teal: #00ab8e;
    --ink: #4a4a4a;
    --paper: #ffffff;
  }
  html, body {
    margin: 0;
    padding: 0;
    width: 1200px;
    height: 800px;
    overflow: hidden;
    background: var(--backdrop);
    font-family: "Lato", sans-serif;
  }
  .stage {
    width: 1200px;
    height: 800px;
    display: flex;
    align-items: center;
    justify-content: center;
    gap: 60px;
  }
  .card {
    width: 500px;
    height: 286px;
    box-sizing: border-box;
    position: relative;
    box-shadow: 0 10px 24px rgba(0,0,0,0.45);
  }
  .card-front {
    background: linear-gradient(90deg, var(--brand-blue-deep), var(--brand-blue-mid));
    display: flex;
    align-items: center;
    justify-content: center;
  }
  .front-name {
    color: var(--paper);
    font-weight: 700;
    font-size: 64px;
    letter-spacing: 1px;
  }
  .card-back {
    background: var(--paper);
    padding: 34px 40px;
  }
  .back-name {
    color: var(--brand-blue);
    font-weight: 700;
    font-size: 38px;
    line-height: 1;
    margin-bottom: 26px;
  }
  .person-name {
    color: var(--brand-blue);
    font-weight: 700;
    font-size: 19px;
  }
  .person-title {
    color: var(--brand-teal);
    font-size: 13px;
    margin-bottom: 14px;
  }
  .address {
    color: var(--ink);
    font-size: 12px;
    line-height: 1.4;
    margin-bottom: 10px;
  }
  .contact-list {
    list-style: none;
    margin: 0;
    padding: 0;
    color: var(--ink);
    font-size: 12px;
  }
  .contact-list li {
    display: flex;
    align-items: center;
    gap: 8px;
    line-height: 1.55;
  }
  .contact-list svg {
    width: 10px;
    height: 10px;
    fill: var(--brand-teal);
    flex: none;
  }
</style>
</head>
<body>
<main class="stage">
  <section class="card card-front">
    <span class="front-name">Velmora</span>
  </section>

  <section class="card card-back">
    <div class="back-name">Velmora</div>
    <div class="person-name">Daniel Marlow, CFA</div>
    <div class="person-title">CEO</div>
    <div class="address">2210 Elmridge Ave.,<br>Suite 410, Harborview, TX 75001</div>
    <ul class="contact-list">
      <li>
        <svg viewBox="0 0 10 10"><path d="M2 0.5 L3.8 2.6 L2.8 3.8 Q4 6 6.2 7.2 L7.4 6.2 L9.5 8 L8.3 9.5 Q3.5 9 0.5 1.7 Z"/></svg>
        555-013-2040
      </li>
      <li>
        <svg viewBox="0 0 10 10"><rect x="0.5" y="2" width="9" height="6.5"/><path d="M0.5 2 L5 5.5 L9.5 2" fill="none" stroke="#fff" stroke-width="0.9"/></svg>
        info@velmoracapital.example
      </li>
      <li>
        <svg viewBox="0 0 10 10"><circle cx="5" cy="5" r="4.5"/></svg>
        www.velmoracapital.example
      </li>
    </ul>
  </section>
</main>
</body>
</html>
```